Flyer Design Project - Nail Art

This is a flyer project for a nail saloon/cosmetics/beauty outlet. The flyer will be double-sided displaying information and/or pictures on both sides.

We would like to have the flyer in C6 format.

Prefered Background of the flyer will be black. Several image will be attached to this description (or may have been already) to help you see what we'd like to see.

FRONT SIDE: On this side we need some Text displayed; informative yet also clearly indicating that it will work as a voucher. Stylish yet professional.

BACK SIDE: Some pictures displayed to allow people to take a look at some of our work. How those pictures are displayed is entirely up to the designer. One idea that we had would be to have four pictures with the logo in the middle - however, this is entirely up to you guys.
Updates

Received a lot of great designs already, thanks!

Will provide feedback starting tomorrow; for now we'll just have a look. Thanks for your patience.

Reason: Only 10 days seemed a bit tight. :) We'll extend the deadline by 5 days.

Hey guys,

something important came up so I can't comment or submit feedback for two days.

Will get back to you all asap.

Cheers!

Reason: Extending the deadline for just a few days! Please do not submit any more designs. Thanks you!

Industry/Entity Type

Cosmetics

Requirements
Must have
• + Text below MUST be included on the front page.
+ C6 Format
+ Pictures displayed on the back
+ Logo Included

TEXT ON THE FRONT SIDE:

KL Glanzwerk - für unvergessliche Hingucker!
Mobiler Service

GUTSCHEIN

NEUANLAGE: 55.- Euro / 65.- CHF (statt 65.- Euro / 80.- CHF)
inklusive French und Verziehrung/Nailart auf 2 Nägel

AUFÜLLEN: 40,- Euro / 50.- CHF (statt 45.- Euro / 55.- CHF)

TERMINE UNTER 0664-5813307

Dieser Flyer dient als Gutschein. Am vereinbarten Termin
vorlegen!

Facebook: KL Glanzwerk
Mail: kl.glanzwerk@postfeld.example
Web: www.kl-glanzwerk.example

-
By designer Request - Rough english Translation of the Flyer text
-

Mobiler Service

[Voucher]
GUTSCHEIN

[Here the prices for completely new sets are listed]
[including French and Nailart on 2 nails]

[here the prices for renewing an existing set are listed]

[Contact telephone number]

[This flyer serves as a voucher. Bring it with you when you have an appointment]
vorlegen!

[Contact Details]
Facebook: KL Glanzwerk
Web: www.kl-glanzwerk.example
Nice to have
• FONT: Beautiful ES

NAILS labeled RED on the front page

PREFERED COLORS: Black/Red

```html
<!DOCTYPE html>
<html lang="de">
<head>
<meta charset="utf-8">
<title>KL Glanzwerk – Gutschein Flyer</title>
<link href="https://fonts.googleapis.com/css2?family=Great+Vibes&display=swap" rel="stylesheet">
<style>
  :root {
    --page: #ffffff;
    --red: #8e1c24;
    --red-deep: #6f1218;
    --charcoal-top: #2a2a2a;
    --charcoal-mid: #4a4a4a;
    --rule: #1a1a1a;
    --ink: #ffffff;
    --accent: #b8353d;
  }
  * { margin: 0; padding: 0; box-sizing: border-box; }
  html, body { width: 933px; height: 1200px; overflow: hidden; background: var(--page); }
  body { position: relative; font-family: "Great Vibes", cursive; color: var(--ink); word-spacing: 4px; }

  .side { position: absolute; left: 64px; width: 807px; height: 582px;
    background: radial-gradient(ellipse at 50% 45%, var(--red) 0%, var(--red-deep) 100%); overflow: hidden; }
  .side--front { top: 0; }
  .side--back { top: 618px; }

  .column { position: absolute; top: 0; bottom: 0;
    background: linear-gradient(180deg, var(--charcoal-top) 0%, var(--charcoal-mid) 55%, var(--charcoal-top) 100%); }
  .side--front .column { left: 497px; width: 253px; }
  .side--back .column { left: 12px; width: 174px; }

  .brand-mark { position: absolute; display: flex; align-items: center; justify-content: center; gap: 8px; white-space: nowrap; }
  .brand-mark .square { width: 12px; height: 12px; background: var(--accent); flex: none; }
  .brand-mark span { color: var(--accent); }
  .side--front .brand-mark { left: 497px; width: 253px; top: 165px; }
  .side--front .brand-mark span { font-size: 28px; }
  .side--back .brand-mark { left: 12px; width: 174px; top: 150px; }
  .side--back .brand-mark span { font-size: 21px; }

  .front-text { position: absolute; left: 30px; top: 22px; width: 445px; text-shadow: 1px 1px 2px rgba(0,0,0,.5); }
  .title { font-size: 34px; line-height: 1.1; display: inline-block; padding-bottom: 6px; border-bottom: 2px solid var(--ink); width: 210px; }
  .tagline { font-size: 27px; margin-top: 18px; }
  .service { font-size: 17px; margin-left: 8px; }
  .prices { font-size: 18px; line-height: 32px; margin-top: 42px; }
  .note { font-size: 17px; margin-top: 24px; text-align: center; }
  .contact { font-size: 20px; line-height: 32px; text-align: center; margin-top: 22px; }

  .thumb { position: absolute; left: 423px; width: 103px; }
  .thumb--one { top: 31px; height: 78px; background: linear-gradient(135deg, #1a0e10, #c89a8a 55%, #2a1416); }
  .thumb--two { top: 128px; height: 78px; background: linear-gradient(135deg, #100a0b, #b97f74 50%, #1a0f10); }

  .voucher-name, .voucher-label { position: absolute; left: 497px; width: 253px; text-align: center; white-space: nowrap; }
  .voucher-name { top: 300px; font-size: 32px; }
  .voucher-label { top: 342px; font-size: 27px; }

  .rule { position: absolute; left: 0; right: 0; height: 4px; background: var(--rule); }
  .rule--top { top: 29px; }
  .rule--bottom { top: 533px; }

  .gallery { position: absolute; left: 219px; top: 76px; display: grid;
    grid-template-columns: 252px 252px; grid-template-rows: 125px 125px 125px; column-gap: 11px; row-gap: 12px; }
  .photo { width: 100%; height: 100%; }
  .photo--green { background: linear-gradient(135deg, #d8cf7a, #b0c24a 50%, #e0c88a); }
  .photo--violet { background: linear-gradient(135deg, #b47c5e, #d8c4b8 55%, #efe6dc); }
  .photo--amber { background: linear-gradient(135deg, #efe5d6, #c88a62 50%, #ece4d8); }
  .photo--black { background: linear-gradient(135deg, #8a5f52, #c8b0a4 50%, #2b2226); }
  .photo--emerald { background: linear-gradient(135deg, #3a3440, #cfb3a4 50%, #245a3c); }
  .photo--rose { background: linear-gradient(135deg, #e6dccf, #d29a9a 50%, #f0e6dc); }

  .back-name { position: absolute; left: 12px; width: 174px; top: 222px; text-align: center; font-size: 26px; white-space: nowrap; }
</style>
</head>
<body>

<section class="side side--front" aria-label="Vorderseite Gutschein">
  <div class="column"></div>

  <div class="front-text">
    <div class="title">KL Glanzwerk</div>
    <p class="tagline">für unvergessliche Hingucker!</p>
    <p class="service">. Mobiler Service</p>
    <p class="prices">
      NEUANLAGE: 55.- Euro / 65.- CHF (statt 65.-<br>
      Euro / 80.- CHF) inklusive French und Verziehrung/<br>
      Nailart auf 2 Nägel<br>
      AUFÜLLEN: 40,- Euro / 50.- CHF (statt 45.-<br>
      Euro / 55.- CHF) inklusive French und Verziehrung/<br>
      Nailart auf 2 Nägel
    </p>
    <p class="note">Dieser Flyer dient als Gutschein. Am vereinbarten Termin vorlegen!</p>
    <p class="contact">
      TERMINE UNTER 0664-5813307<br>
      Facebook: KL Glanzwerk Mail: kl.glanzwerk@postfeld.example<br>
      Web: www.kl-glanzwerk.example
    </p>
  </div>

  <div class="thumb thumb--one" role="img" aria-label="Foto: Hand mit roten Nägeln"></div>
  <div class="thumb thumb--two" role="img" aria-label="Foto: Hände mit roter Nailart"></div>

  <div class="brand-mark"><div class="square"></div><span>KL Glanzwerk</span></div>

  <div class="voucher-name">KL Glanzwerk</div>
  <div class="voucher-label">GUTSCHEIN</div>
</section>

<section class="side side--back" aria-label="Rückseite Arbeiten">
  <div class="column"></div>
  <div class="rule rule--top"></div>
  <div class="rule rule--bottom"></div>

  <div class="brand-mark"><div class="square"></div><span>KL Glanzwerk</span></div>
  <div class="back-name">KL Glanzwerk</div>

  <div class="gallery">
    <div class="photo photo--green" role="img" aria-label="Foto: Nägel mit grüner French-Spitze"></div>
    <div class="photo photo--violet" role="img" aria-label="Foto: Nägel mit violetter Verzierung"></div>
    <div class="photo photo--amber" role="img" aria-label="Foto: Nägel mit orangefarbener Nailart"></div>
    <div class="photo photo--black" role="img" aria-label="Foto: Nägel mit schwarzer French-Spitze"></div>
    <div class="photo photo--emerald" role="img" aria-label="Foto: Nägel in Violett und Grün"></div>
    <div class="photo photo--rose" role="img" aria-label="Foto: Nägel mit rosa-roter Spitze"></div>
  </div>
</section>

</body>
</html>
```